Equity, Effectiveness and Efficiency in charitable food relief sector

I am undertaking my PhD in food policy in the charitable food relief sector, specifically investigating the factors (supply, demand and capacity) that affect the introduction of nutrition policy and in turn, affect the sector's ability to achieve equity, effectiveness and efficiency.

I need a graphic device that incorporates this central idea of Equity, Effectiveness and Efficiency, and how the factors of supply, demand and capacity interact. There are sub-factors within supply (1-6), demand (7-10) and capacity (11 - 15). All these details are shown in the attached figure (Basic figure_Eq Effec Effic and factors.jpg)

This figure (Basic figure_Eq Effec Effic and factors.jpg) contains all the information I need in a graphic but I need something that is more visually appealing, and that can link the ideas in a format other than a table. The final graphic will outline how the food relief sector balances the core objectives of equity, effectiveness and efficiency with the factors (and sub-factors) of supply, demand and capacity.

```html
<!DOCTYPE html>
<html lang="en">
<head>
<meta charset="utf-8">
<title>Equity, Effectiveness, Efficiency — Food Relief Factors</title>
<link href="https://fonts.googleapis.com/css2?family=Source+Sans+3:wght@500;600;700&display=swap" rel="stylesheet">
<style>
  :root {
    --dark: #33213f;
    --pink: #e8217a;
    --magenta: #b52a88;
    --purple: #7a3596;
    --violet: #5e3b9c;
    --title-end: #3f48a0;
    --silver: #c9c9d1;
    --white: #ffffff;
    --supply-red: #ee1111;
    --demand-amber: #f5a93a;
    --capacity-green: #3db44a;
  }
  * { box-sizing: border-box; margin: 0; padding: 0; }
  html, body { width: 1200px; height: 675px; overflow: hidden; background: var(--dark); }
  .canvas {
    position: relative; width: 1200px; height: 675px; overflow: hidden;
    font-family: "Source Sans 3", sans-serif; color: var(--white);
  }
  .backdrop { position: absolute; inset: 0; }
  .title {
    position: absolute; left: 202px; top: 24px; width: 796px; height: 65px;
    border: 3px solid var(--silver); border-radius: 22px;
    background: linear-gradient(90deg, var(--pink), var(--purple) 55%, var(--title-end));
    box-shadow: 0 4px 8px rgba(0,0,0,.3);
    display: flex; align-items: center; justify-content: center;
    font-weight: 700; font-size: 45px; letter-spacing: -0.3px; line-height: 1;
    white-space: nowrap; overflow: hidden;
  }
  .factor-label {
    position: absolute; height: 49px; border: 3px solid var(--silver); border-radius: 14px;
    display: flex; align-items: center; justify-content: center;
    font-weight: 700; font-size: 33px; line-height: 1; white-space: nowrap;
    box-shadow: 0 4px 8px rgba(0,0,0,.35);
  }
  .factor-label.supply { left: 231px; top: 283px; width: 164px; background: var(--supply-red); font-size: 31px; }
  .factor-label.demand { left: 517px; top: 321px; width: 165px; background: var(--demand-amber); }
  .factor-label.capacity { left: 804px; top: 285px; width: 166px; background: var(--capacity-green); }
  .icon-box {
    position: absolute; width: 43px; height: 43px;
    border: 2px solid var(--silver); border-radius: 9px;
  }
  .icon-box svg { width: 100%; height: 100%; display: block; }
  .item {
    position: absolute; font-weight: 600; font-size: 16.3px; line-height: 18.2px; white-space: nowrap;
  }
  .item .sub { display: block; padding-left: 16px; }
  .item .cont { display: block; padding-left: 16px; }
  .item.sublist .sub { padding-left: 23px; line-height: 20px; }
</style>
</head>
<body>
<div class="canvas">
  <svg class="backdrop" width="1200" height="675" viewBox="0 0 1200 675">
    <defs>
      <linearGradient id="stage" x1="0" y1="0" x2="1" y2="0.6">
        <stop offset="0" stop-color="#ea227b"/>
        <stop offset="0.45" stop-color="#a82b8c"/>
        <stop offset="1" stop-color="#5c3c9e"/>
      </linearGradient>
    </defs>
    <rect width="1200" height="675" fill="var(--dark)"/>
    <circle cx="600" cy="53" r="688" fill="url(#stage)"/>
    <g stroke="var(--silver)" stroke-width="4" fill="none">
      <polyline points="313,152 313,111 887,111 887,152"/>
      <line x1="600" y1="111" x2="600" y2="186"/>
    </g>
    <g fill="#e8e8ee">
      <polygon points="302,134 324,134 313,158"/>
      <polygon points="876,134 898,134 887,158"/>
      <polygon points="589,168 611,168 600,194"/>
    </g>
    <g stroke="var(--silver)" stroke-width="3" fill="none">
      <circle cx="313" cy="221" r="53"/>
      <circle cx="600" cy="258" r="53"/>
      <circle cx="887" cy="219" r="53"/>
    </g>
    <g stroke="var(--white)" stroke-width="3" fill="none" stroke-linejoin="round" stroke-linecap="round">
      <path d="M278 200 L348 200 L340 232 L286 232 Z"/>
      <line x1="287" y1="242" x2="345" y2="242"/>
      <line x1="286" y1="232" x2="287" y2="242"/>
      <line x1="340" y1="232" x2="341" y2="242"/>
      <circle cx="290" cy="245" r="5"/>
      <circle cx="337" cy="245" r="5"/>
    </g>
    <path d="M283 205 L343 205 L337 228 L289 228 Z" fill="var(--white)"/>
    <g stroke="var(--white)" stroke-width="3" fill="none" stroke-linecap="round">
      <line x1="568" y1="226" x2="568" y2="288"/>
      <line x1="568" y1="288" x2="632" y2="288"/>
      <circle cx="589" cy="240" r="8"/>
      <polyline points="568,262 585,250 600,264 614,254 632,242"/>
      <polyline points="624,241 635,239 632,250"/>
    </g>
    <g stroke="var(--white)" stroke-width="2">
      <line x1="574" y1="270" x2="574" y2="286"/><line x1="580" y1="266" x2="580" y2="286"/>
      <line x1="586" y1="262" x2="586" y2="286"/><line x1="592" y1="262" x2="592" y2="286"/>
      <line x1="598" y1="268" x2="598" y2="286"/><line x1="604" y1="266" x2="604" y2="286"/>
      <line x1="610" y1="260" x2="610" y2="286"/><line x1="616" y1="256" x2="616" y2="286"/>
      <line x1="622" y1="252" x2="622" y2="286"/><line x1="628" y1="248" x2="628" y2="286"/>
    </g>
    <g stroke="var(--white)" stroke-width="3" fill="none" stroke-linejoin="round">
      <rect x="850" y="194" width="44" height="42"/>
      <path d="M894 204 L912 204 L925 222 L925 238 L894 238"/>
      <path d="M899 208 L910 208 L918 220 L899 220 Z"/>
      <rect x="856" y="200" width="9" height="28"/>
      <rect x="869" y="200" width="9" height="28"/>
      <line x1="850" y1="238" x2="894" y2="238"/>
      <circle cx="867" cy="240" r="7"/>
      <circle cx="907" cy="240" r="7"/>
    </g>
  </svg>

  <div class="title">EQUITY, EFFECTIVENESS, EFFICIENCY</div>
  <div class="factor-label supply">SUPPLY</div>
  <div class="factor-label demand">DEMAND</div>
  <div class="factor-label capacity">CAPACITY</div>

  <!-- Supply factors -->
  <div class="icon-box" style="left:66px;top:156px">
    <svg viewBox="0 0 42 42" fill="none" stroke="#fff" stroke-width="1.6"><rect x="9" y="15" width="24" height="12"/><rect x="14" y="11" width="14" height="4"/><line x1="9" y1="21" x2="33" y2="21"/><line x1="17" y1="15" x2="17" y2="27"/><line x1="25" y1="15" x2="25" y2="27"/><line x1="7" y1="29" x2="35" y2="29"/><circle cx="11" cy="32" r="2"/><circle cx="31" cy="32" r="2"/></svg>
  </div>
  <div class="item" style="left:111px;top:152px">1. Uncertain<span class="cont">Material</span><span class="cont">Suply</span></div>

  <div class="icon-box" style="left:73px;top:228px">
    <svg viewBox="0 0 42 42" fill="none" stroke="#fff" stroke-width="1.6"><rect x="9" y="14" width="26" height="16"/><path d="M5 22 L10 10 L16 12"/><circle cx="22" cy="22" r="5"/><text x="22" y="25.5" font-size="8" text-anchor="middle" fill="#fff" stroke="none" font-family="sans-serif">$</text></svg>
  </div>
  <div class="item" style="left:124px;top:222px">2. Uncertain<span class="cont">Monetary</span><span class="cont">Suply</span></div>

  <div class="icon-box" style="left:98px;top:307px">
    <svg viewBox="0 0 42 42" fill="none" stroke="#fff" stroke-width="1.8" stroke-linecap="round"><circle cx="21" cy="21" r="14"/><line x1="17" y1="13" x2="17" y2="30"/><path d="M14 13 V19 Q17 22 20 19 V13"/><path d="M25 30 V13 Q29 16 28 23 H25"/></svg>
  </div>
  <div class="item" style="left:146px;top:304px">3. Limited<span class="cont">Food</span><span class="cont">Suply</span></div>

  <div class="icon-box" style="left:137px;top:382px">
    <svg viewBox="0 0 42 42" fill="none" stroke="#fff" stroke-width="1.6" stroke-linecap="round"><rect x="10" y="6" width="5" height="4"/><path d="M10 10 L8 16 V34 H17"/><circle cx="24" cy="26" r="9" stroke-dasharray="3 2"/><polyline points="24,20 24,26 28,29"/></svg>
  </div>
  <div class="item" style="left:184px;top:395px">4. Perishability</div>

  <div class="icon-box" style="left:163px;top:439px">
    <svg viewBox="0 0 42 42" fill="#fff"><circle cx="21" cy="21" r="6"/><circle cx="21" cy="9" r="2"/><circle cx="29.5" cy="12.5" r="2"/><circle cx="33" cy="21" r="2"/><circle cx="29.5" cy="29.5" r="2"/><circle cx="21" cy="33" r="2"/><circle cx="12.5" cy="29.5" r="2"/><circle cx="9" cy="21" r="2"/><circle cx="12.5" cy="12.5" r="2"/></svg>
  </div>
  <div class="item" style="left:215px;top:448px">5. Donor Constraints</div>

  <div class="icon-box" style="left:217px;top:495px">
    <svg viewBox="0 0 42 42" fill="none" stroke="#fff" stroke-width="1.6" stroke-linejoin="round"><path d="M21 34 L8 21 Q4 15 9 10 Q15 6 21 13 Q27 6 33 10 Q38 15 34 21 Z"/><line x1="14" y1="24" x2="22" y2="17"/><line x1="17" y1="27" x2="25" y2="20"/><line x1="20" y1="30" x2="28" y2="23"/></svg>
  </div>
  <div class="item" style="left:266px;top:503px">6. Donor Relationships</div>

  <!-- Demand factors -->
  <div class="icon-box" style="left:467px;top:386px">
    <svg viewBox="0 0 42 42" fill="none" stroke="#fff" stroke-width="1.8" stroke-linejoin="round"><polyline points="6,27 14,18 21,22 30,14 36,12"/><polyline points="6,24 12,22 20,27 28,24 36,20"/><circle cx="14" cy="18" r="1.5" fill="#fff"/><circle cx="30" cy="14" r="1.5" fill="#fff"/><circle cx="20" cy="27" r="1.5" fill="#fff"/></svg>
  </div>
  <div class="item" style="left:522px;top:397px">7. Uncertain Demand</div>

  <div class="icon-box" style="left:467px;top:438px">
    <svg viewBox="0 0 42 42" fill="none" stroke="#fff" stroke-width="2"><path d="M15 18 V14 Q21 6 27 14 V18"/><rect x="12" y="18" width="18" height="14" fill="#fff"/><circle cx="21" cy="25" r="1.8" fill="#7a3596" stroke="none"/></svg>
  </div>
  <div class="item" style="left:522px;top:453px">8. Limited Demand Visibility</div>

  <div class="icon-box" style="left:467px;top:490px">
    <svg viewBox="0 0 42 42" fill="none" stroke="#fff" stroke-width="1.6" stroke-linecap="round"><rect x="12" y="12" width="17" height="20"/><line x1="15" y1="10" x2="15" y2="14"/><line x1="19" y1="10" x2="19" y2="14"/><line x1="23" y1="10" x2="23" y2="14"/><polyline points="18,24 22,28 31,18" stroke-width="2.4"/></svg>
  </div>
  <div class="item" style="left:522px;top:503px">9. Client Choice</div>

  <div class="icon-box" style="left:467px;top:542px">
    <svg viewBox="0 0 42 42" fill="none" stroke="#fff" stroke-width="1.6"><rect x="13" y="20" width="16" height="16" fill="#fff"/><rect x="11" y="16" width="20" height="4" fill="#fff"/><line x1="17" y1="24" x2="17" y2="33" stroke="#7a3596"/><line x1="21" y1="24" x2="21" y2="33" stroke="#7a3596"/><line x1="25" y1="24" x2="25" y2="33" stroke="#7a3596"/><path d="M20 16 Q20 10 25 8" /></svg>
  </div>
  <div class="item" style="left:514px;top:556px">10. Food Wastage</div>

  <!-- Capacity factors -->
  <div class="icon-box" style="left:1115px;top:154px">
    <svg viewBox="0 0 42 42" fill="none" stroke="#fff" stroke-width="1.8" stroke-linejoin="round"><polyline points="6,20 21,8 36,20"/><path d="M10 17 V34 H32 V17"/><rect x="14" y="20" width="14" height="12" fill="#fff"/><g stroke="#7a3596" stroke-width="1"><line x1="14" y1="24" x2="28" y2="24"/><line x1="14" y1="28" x2="28" y2="28"/><line x1="19" y1="20" x2="19" y2="32"/><line x1="24" y1="20" x2="24" y2="32"/></g></svg>
  </div>
  <div class="item sublist" style="left:989px;top:148px">11. Storage<span class="sub">a) Cold</span><span class="sub">b) Warehouse</span></div>

  <div class="icon-box" style="left:1108px;top:239px">
    <svg viewBox="0 0 42 42" fill="#fff"><path d="M21 6 Q23 6 23 10 V17 L35 24 V27 L23 23 V31 L27 34 V36 L21 34.5 L15 36 V34 L19 31 V23 L7 27 V24 L19 17 V10 Q19 6 21 6 Z"/></svg>
  </div>
  <div class="item" style="left:973px;top:250px">12. Transportation</div>

  <div class="icon-box" style="left:1086px;top:346px">
    <svg viewBox="0 0 42 42" fill="#fff"><circle cx="21" cy="9" r="2.5"/><path d="M17 16 Q21 11 25 16 Z"/><circle cx="16" cy="18" r="2.5"/><circle cx="26" cy="18" r="2.5"/><path d="M12 25 Q16 20 20 25 Z"/><path d="M22 25 Q26 20 30 25 Z"/><circle cx="11" cy="27" r="2.5"/><circle cx="21" cy="27" r="2.5"/><circle cx="31" cy="27" r="2.5"/><path d="M7 34 Q11 29 15 34 Z"/><path d="M17 34 Q21 29 25 34 Z"/><path d="M27 34 Q31 29 35 34 Z"/></svg>
  </div>
  <div class="item sublist" style="left:880px;top:348px">13. Workforce<span class="sub">a) Volunteers</span><span class="sub">b) Expertise and Training</span><span class="sub">c) Attitudes</span><span class="sub">d) Collaboration</span><span class="sub">e) Executive Support</span></div>

  <div class="icon-box" style="left:1024px;top:479px">
    <svg viewBox="0 0 42 42" fill="none" stroke="#fff" stroke-width="1.3"><circle cx="21" cy="11" r="3"/><circle cx="12" cy="19" r="2.5"/><circle cx="30" cy="19" r="2.5"/><path d="M6 27 Q12 21 18 27"/><path d="M24 27 Q30 21 36 27"/><path d="M17 18 Q21 14 25 18"/><rect x="15" y="24" width="12" height="6"/><line x1="6" y1="31" x2="36" y2="31"/><line x1="9" y1="31" x2="8" y2="35"/><line x1="33" y1="31" x2="34" y2="35"/></svg>
  </div>
  <div class="item" style="left:843px;top:488px">14. External Stakeholders</div>

  <div class="icon-box" style="left:890px;top:537px">
    <svg viewBox="0 0 42 42" fill="none" stroke="#fff" stroke-width="1.8"><rect x="11" y="7" width="20" height="28" rx="2"/><rect x="14" y="10" width="14" height="5"/><g fill="#fff" stroke="none"><circle cx="15.5" cy="20" r="1.6"/><circle cx="21" cy="20" r="1.6"/><circle cx="26.5" cy="20" r="1.6"/><circle cx="15.5" cy="25" r="1.6"/><circle cx="21" cy="25" r="1.6"/><circle cx="26.5" cy="25" r="1.6"/><circle cx="15.5" cy="30" r="1.6"/><circle cx="21" cy="30" r="1.6"/><circle cx="26.5" cy="30" r="1.6"/></g></svg>
  </div>
  <div class="item" style="left:803px;top:549px">15. Budget</div>
</div>
</body>
</html>
```